個人で販売しております沖縄のお菓子のラベルデザインをお願いします。

島のおやつ 「黒糖アガラサー」は、蒸しパンのような保存料不使用で、お年寄りからお子さんまで安心してお召し上がられます。一口食べてほこっりし、懐かしい味わいです。

お店の名前の由来でもある、沖縄の葉「月桃」をイメージしほっこりする感じに作成して頂きたいです。素敵なロゴの作成お願いします。

個人事業所なので、何もかもがわからないことだらけですが、どうぞよろしくお願い致します。

黒糖アガラサーも添付しております。

提案されたものに、入れたいと思っていたものが全部入っていたことが選んだ理由です。
そして、安価の予算にも関わらず修正も何度も引き受けて頂き感謝です。
最終納品時にはお手数おかけしましたが、本当にありがとうございました。

提案して頂きましたミルダーの皆さん、初めての依頼で手こずってしまって
当選結果が遅れたことをお詫び申しあげます。
そして、素敵な提案して頂きましたことに感謝いたします。
本当にありがとうございました。

```html
<!DOCTYPE html>
<html lang="ja">
<head>
<meta charset="utf-8">
<title>黒糖アガラサー ラベル</title>
<link rel="stylesheet" href="https://fonts.googleapis.com/css2?family=M+PLUS+Rounded+1c:wght@800&family=Yusei+Magic&family=Noto+Sans+JP:wght@500&display=swap">
<style>
  :root{
    --bg:#ffffff;
    --label-white:#ffffff;
    --frame-green:#7fae4a;
    --leaf-light:#e6f1ea;
    --leaf-mid:#9fcab3;
    --leaf-deep:#5f9f86;
    --badge-orange:#d9703c;
    --ink:#161616;
    --kana-a:#7a2630;
    --kana-ga:#7e3f8f;
    --kana-ra:#a83c4c;
    --kana-sa:#8c2b37;
    --kana-bar:#7a2630;
  }
  html,body{margin:0;padding:0;width:1200px;height:884px;overflow:hidden;background:var(--bg);}
  .label{display:block;width:1200px;height:884px;}
  .label-body{fill:var(--label-white);filter:drop-shadow(0 6px 10px rgba(0,0,0,.28));}
  .label-frame{fill:none;stroke:var(--frame-green);stroke-width:4;}
  .badge{fill:var(--badge-orange);}
  .badge-text{font-family:"Yusei Magic",sans-serif;fill:#fff;text-anchor:middle;}
  .kanji-title{font-family:"M PLUS Rounded 1c",sans-serif;font-weight:800;fill:var(--ink);
    stroke:#fff;stroke-width:8;paint-order:stroke;stroke-linejoin:round;}
  .product-name{font-family:"Yusei Magic",sans-serif;font-size:104px;
    stroke:#fff;stroke-width:10;paint-order:stroke;stroke-linejoin:round;}
  .tagline{font-family:"Noto Sans JP",sans-serif;font-weight:500;font-size:44px;fill:var(--ink);text-anchor:middle;}
</style>
</head>
<body>
<svg class="label" viewBox="0 0 1000 737" xmlns="http://www.w3.org/2000/svg">
  <defs>
    <path id="bean" d="M175 260 C190 185 330 170 430 200 C500 220 540 220 600 165 C660 110 780 105 840 150 C900 200 895 330 870 420 C840 530 760 610 560 625 C380 635 200 620 150 500 C120 420 155 320 175 260 Z"/>
    <linearGradient id="leafTone" x1="0" y1="0" x2="1" y2="1">
      <stop offset="0" stop-color="var(--leaf-light)"/>
      <stop offset=".45" stop-color="var(--leaf-mid)"/>
      <stop offset=".7" stop-color="var(--leaf-deep)" stop-opacity=".7"/>
      <stop offset="1" stop-color="var(--leaf-light)"/>
    </linearGradient>
    <clipPath id="innerClip"><use href="#bean" transform="translate(505 380) scale(.955) translate(-505 -380)"/></clipPath>
  </defs>

  <use class="label-body" href="#bean" transform="translate(505 380) scale(1.03) translate(-505 -380)"/>

  <g clip-path="url(#innerClip)">
    <rect x="100" y="90" width="820" height="560" fill="url(#leafTone)" role="img" aria-label="月桃の葉の水彩イラスト"/>
  </g>
  <use class="label-frame" href="#bean" transform="translate(505 380) scale(.955) translate(-505 -380)"/>

  <g class="island-badge">
    <circle class="badge" cx="730" cy="224" r="70"/>
    <circle class="badge" cx="680" cy="302" r="10"/>
    <circle class="badge" cx="663" cy="318" r="7"/>
    <text class="badge-text" x="738" y="212" font-size="50">島</text>
    <text class="badge-text" x="730" y="268" font-size="40" textLength="118" lengthAdjust="spacingAndGlyphs">おやつ</text>
  </g>

  <text class="kanji-title" x="176" y="342" font-size="66">黒</text>
  <text class="kanji-title" x="176" y="432" font-size="66">糖</text>

  <text class="product-name" x="335" y="440" textLength="450" lengthAdjust="spacingAndGlyphs">
    <tspan fill="var(--kana-a)">ア</tspan><tspan fill="var(--kana-ga)">ガ</tspan><tspan fill="var(--kana-ra)">ラ</tspan><tspan fill="var(--kana-sa)">サ</tspan><tspan fill="var(--kana-bar)">ー</tspan>
  </text>

  <text class="tagline" x="472" y="562">保存料不使用</text>
</svg>
</body>
</html>
```